Update Law Firm Website

Update law firm website pages, add pages for employees. Current website looks stale. www.lowrevanlaw.com

Target Market(s)

Personal injury clients

Industry/Entity Type

Legal

Number of Pages Required

5+ page

Font styles to use
Serif

Requirements
Must have
• User friendly and engaging design
Nice to have
• ?
Should not have
• scales of justice, law books,

```html
<!DOCTYPE html>
<html lang="en">
<head>
<meta charset="utf-8">
<title>Harborline Injury Law Group</title>
<link href="https://fonts.googleapis.com/css2?family=Open+Sans:ital,wght@0,400;0,600;0,700;1,400&family=Roboto+Condensed:wght@400;700&family=Tinos&display=swap" rel="stylesheet">
<style>
:root{
  --orange:#e8692d;
  --ink:#1e2233;
  --text:#555a60;
  --nav:#1d1e20;
  --card:#f2f2f2;
  --card-line:#dcdcdc;
  --icon:#4a4c50;
  --white:#ffffff;
  --rule:#e4e4e4;
}
*{margin:0;padding:0;box-sizing:border-box}
html,body{width:1200px;height:2384px;overflow:hidden;background:var(--white)}
body{position:relative;font-family:"Open Sans",Arial,sans-serif;color:var(--text)}

/* header */
.site-header{position:absolute;left:0;top:0;width:1200px;height:102px;background:var(--white)}
.brand{position:absolute;left:99px;top:26px;display:flex;align-items:center;gap:18px}
.brand-mark{width:52px;height:52px;background:var(--orange)}
.brand-name{font-family:"Tinos",Georgia,serif;font-size:27px;color:var(--ink);letter-spacing:.3px;line-height:1}
.brand-sub{font-family:"Tinos",Georgia,serif;font-size:16px;color:var(--orange);margin-top:8px;letter-spacing:.4px}
.call{position:absolute;left:677px;top:32px;display:flex;align-items:center;gap:14px;font-size:13px;color:#333}
.call-icon{width:38px;height:38px;border-radius:50%;background:var(--orange);display:flex;align-items:center;justify-content:center}
.btn{display:flex;align-items:center;justify-content:center;background:var(--orange);color:var(--white);font-weight:700;font-size:13px;letter-spacing:.3px;border-radius:2px}
.consult-btn{position:absolute;left:912px;top:32px;width:189px;height:40px}

/* nav */
.main-nav{position:absolute;left:0;top:102px;width:1200px;height:44px;background:var(--nav);display:flex;align-items:center;gap:55px;padding-left:100px}
.main-nav a{color:var(--white);text-decoration:none;font-size:12px;font-weight:700}

/* hero */
.hero{position:absolute;left:0;top:146px;width:1200px;height:514px;
  background:
    linear-gradient(180deg,rgba(20,14,12,0) 0%,rgba(20,14,12,0) 70%,rgba(30,18,12,.85) 84%,rgba(28,20,16,.95) 100%),
    radial-gradient(ellipse 260px 160px at 660px 380px,rgba(255,214,120,.95) 0%,rgba(255,160,60,.6) 45%,rgba(255,140,40,0) 100%),
    radial-gradient(ellipse 300px 90px at 820px 90px,rgba(40,26,22,.85) 0%,rgba(40,26,22,0) 100%),
    radial-gradient(ellipse 260px 80px at 200px 170px,rgba(50,30,22,.7) 0%,rgba(50,30,22,0) 100%),
    linear-gradient(180deg,#4a3528 0%,#8a4a24 22%,#d4702c 45%,#f08a32 62%,#b5531e 76%,#3a2418 100%)}
.hero-title{position:absolute;left:91px;top:340px;font-family:"Roboto Condensed",Arial,sans-serif;font-weight:400;font-size:49px;color:var(--white);letter-spacing:.5px;line-height:1.1}
.hero-text{position:absolute;left:92px;top:400px;width:570px;font-size:15.5px;line-height:28px;color:var(--white)}
.hero-dots{position:absolute;left:574px;top:486px;display:flex;gap:6px}
.hero-dots span{width:8px;height:8px;border-radius:50%;background:#9a9a9a}
.hero-dots span:first-child{background:var(--orange)}

/* intro */
.intro-title{position:absolute;left:0;top:720px;width:1200px;text-align:center;font-size:27px;font-weight:700;color:var(--ink)}
.intro-text{position:absolute;left:210px;top:772px;width:780px;text-align:center;font-size:14px;line-height:27px;color:var(--text)}

/* practice cards */
.card{position:absolute;top:914px;width:238px;height:245px;background:var(--card);border:1px solid var(--card-line);text-align:center;border-radius:2px}
.card::after{content:"";position:absolute;left:34px;right:34px;bottom:-18px;height:10px;border-radius:50%;background:radial-gradient(ellipse,rgba(0,0,0,.18),rgba(0,0,0,0) 70%)}
.card.is-active{background:var(--orange);border-color:var(--orange)}
.card-icon{display:block;width:100px;height:90px;margin:24px auto 0;color:var(--icon)}
.card.is-active .card-icon{color:var(--white)}
.card-title{margin-top:22px;font-size:16px;font-weight:600;color:#33363c}
.card-text{margin-top:10px;font-size:12.5px;line-height:22px;color:#6a6d72}
.card.is-active .card-title,.card.is-active .card-text{color:var(--white)}

/* attorney */
.portrait-ring{position:absolute;left:99px;top:1255px;width:336px;height:336px;border-radius:50%;background:#f4f4f4;border:1px solid #e2e2e2}
.portrait{position:absolute;left:111px;top:1267px;width:312px;height:312px;border-radius:50%;
  background:
    linear-gradient(180deg,rgba(20,20,24,0) 0%,rgba(20,20,24,0) 62%,rgba(22,22,26,.95) 78%,#18181c 100%),
    radial-gradient(ellipse 120px 150px at 50% 42%,rgba(150,120,100,.55) 0%,rgba(150,120,100,0) 100%),
    radial-gradient(circle at 30% 30%,#5a6258 0%,#3e4440 55%,#2a2e2c 100%)}
.bio-title{position:absolute;left:509px;top:1262px;font-size:27px;font-weight:700;color:var(--ink);letter-spacing:.3px}
.bio-sub{position:absolute;left:509px;top:1304px;font-size:15px;color:#333}
.bio-text{position:absolute;left:509px;width:595px;font-size:12.5px;line-height:25px;color:var(--text)}
.more-btn{position:absolute;left:509px;top:1544px;width:165px;height:46px;font-size:13px}

/* testimonial */
.testimonials{position:absolute;left:0;top:1677px;width:1200px;height:421px;
  background:
    radial-gradient(ellipse 180px 420px at 600px 421px,rgba(70,70,72,.9) 0%,rgba(70,70,72,0) 100%),
    radial-gradient(ellipse 700px 90px at 600px 120px,rgba(170,120,80,.55) 0%,rgba(170,120,80,0) 100%),
    linear-gradient(180deg,#3e342e 0%,#6a5444 22%,#3a302a 34%,#2a2522 48%,#3a3a3a 75%,#2e2e2e 100%)}
.t-title{position:absolute;left:0;top:70px;width:1200px;text-align:center;font-size:26px;font-weight:700;color:var(--white)}
.t-quote{position:absolute;left:229px;top:174px;width:470px;font-size:12.5px;line-height:28px;font-style:italic;color:var(--white)}
.t-mark{position:absolute;font-family:"Tinos",Georgia,serif;font-size:56px;color:#8a8a8a;line-height:1}
.t-name{position:absolute;left:229px;top:290px;font-size:13px;font-weight:700;color:var(--orange)}
.t-role{position:absolute;left:229px;top:314px;font-size:12px;color:var(--white)}
.t-photo{position:absolute;left:789px;top:147px;width:184px;height:184px;border-radius:50%;
  background:
    linear-gradient(180deg,rgba(30,30,30,0) 0%,rgba(30,30,30,0) 78%,#2a2a2a 90%),
    radial-gradient(ellipse 60px 75px at 50% 45%,rgba(214,170,140,.8) 0%,rgba(214,170,140,0) 100%),
    radial-gradient(circle,#f2f2f2 0%,#dcdcdc 100%);border:3px solid #f0f0f0}
.t-arrow{position:absolute;top:196px}

/* footer */
.footer-col{position:absolute;top:2141px}
.footer-head{font-size:14px;font-weight:700;color:#222;line-height:19px}
.footer-list{list-style:none;margin-top:10px}
.footer-list li{font-size:12px;line-height:24px;color:#555}
.social{position:absolute;left:908px;top:2196px;display:flex;gap:8px}
.social span{width:28px;height:28px;border-radius:50%;background:#cfcfcf}
.email-btn{position:absolute;left:673px;top:2258px;width:82px;height:25px;font-size:11px}
.footer-rule{position:absolute;left:0;top:2325px;width:1200px;height:1px;background:var(--rule)}
.copyright{position:absolute;left:0;top:2342px;width:1200px;text-align:center;font-size:11px;color:#555}
</style>
</head>
<body>

<header class="site-header">
  <div class="brand">
    <div class="brand-mark"></div>
    <div>
      <div class="brand-name">HARBORLINE INJURY LAW GROUP</div>
      <div class="brand-sub">DANIEL R. MARLOWE, ESQUIRE</div>
    </div>
  </div>
  <div class="call">
    <div class="call-icon">
      <svg width="16" height="16" viewBox="0 0 24 24"><path fill="#fff" d="M6.6 10.8c1.4 2.8 3.8 5.1 6.6 6.6l2.2-2.2c.3-.3.7-.4 1-.2 1.1.4 2.3.6 3.6.6.6 0 1 .4 1 1V20c0 .6-.4 1-1 1C10.6 21 3 13.4 3 4c0-.6.4-1 1-1h3.5c.6 0 1 .4 1 1 0 1.3.2 2.5.6 3.6.1.3 0 .7-.2 1z"/></svg>
    </div>
    <span>CALL US : (555) 014-2290</span>
  </div>
  <div class="btn consult-btn">FREE CONSULTATION</div>
</header>

<nav class="main-nav">
  <a>SLIP AND FALL</a>
  <a>AUTO ACCIDENT</a>
  <a>CONSTRUCTION INJURIES</a>
  <a>MEDICAL MALPRACTICE</a>
  <a>RESULTS</a>
  <a>ABOUT US</a>
  <a>CONTACT US</a>
</nav>

<section class="hero" role="img" aria-label="Suspension bridge over a river with the city skyline at sunset">
  <h1 class="hero-title">DANIEL R. MARLOWE</h1>
  <p class="hero-text">We take all cases on a contingency basis,meaning you will not pay attorney fees or costs unless we recover on your behalf.</p>
  <div class="hero-dots"><span></span><span></span><span></span><span></span></div>
</section>

<h2 class="intro-title">HARBORLINE INJURY LAW GROUP</h2>
<p class="intro-text">Daniel R. Marlowe has successfully handled death and serious personal injury cases involving automobiles and tractor trailers, injuries caused by toxic products, pipeline explosion cases, slip and fall cases involving commercial businesses, and cases against insurance companies.</p>

<div class="card is-active" style="left:99px">
  <svg class="card-icon" viewBox="0 0 100 90" role="img" aria-label="Slip and fall icon">
    <circle cx="66" cy="20" r="8" fill="currentColor"/>
    <path d="M60 30 40 46M46 40l20 6M40 46l-8 18h-12M40 46l16 12-6 18" fill="none" stroke="currentColor" stroke-width="8" stroke-linecap="round" stroke-linejoin="round"/>
    <path d="M28 10a14 14 0 0 1 16-4" fill="none" stroke="currentColor" stroke-width="3" stroke-linecap="round"/>
  </svg>
  <div class="card-title">SLIP AND FALL</div>
  <div class="card-text">For a Free Case Evaluation,<br>contact us today</div>
</div>
<div class="card" style="left:353px">
  <svg class="card-icon" viewBox="0 0 100 90" role="img" aria-label="Car collision icon">
    <path d="M6 62v-12l10-4 12-12h26l14 12 10 2v14z" fill="currentColor"/>
    <path d="M32 38h9v8H24zM45 38h8l8 8H45z" fill="#f2f2f2"/>
    <circle cx="22" cy="64" r="8" fill="currentColor" stroke="#f2f2f2" stroke-width="3"/>
    <circle cx="64" cy="64" r="8" fill="currentColor" stroke="#f2f2f2" stroke-width="3"/>
    <path d="M82 20l3 12 10-6-5 11 9 4-11 3 4 10-9-6-4 8" fill="none" stroke="currentColor" stroke-width="4" stroke-linejoin="round"/>
  </svg>
  <div class="card-title">AUTO ACCIDENT</div>
  <div class="card-text">For a Free Case Evaluation,<br>contact us today</div>
</div>
<div class="card" style="left:609px">
  <svg class="card-icon" viewBox="0 0 100 90" role="img" aria-label="Injured worker icon">
    <circle cx="50" cy="24" r="16" fill="currentColor"/>
    <path d="M24 86V60c0-10 8-16 18-16h16c10 0 18 6 18 16v26z" fill="currentColor"/>
    <path d="M40 46l26 26H38" fill="none" stroke="#f2f2f2" stroke-width="4" stroke-linejoin="round"/>
  </svg>
  <div class="card-title">CONSTRUCTION INJURIES</div>
  <div class="card-text">For a Free Case Evaluation,<br>contact us today</div>
</div>
<div class="card" style="left:863px">
  <svg class="card-icon" viewBox="0 0 100 90" role="img" aria-label="Stethoscope icon">
    <path d="M26 8v20c0 12 8 20 18 20s18-8 18-20V8" fill="none" stroke="currentColor" stroke-width="4" stroke-linecap="round"/>
    <path d="M44 48v14c0 12 10 20 22 16s14-18 6-26" fill="none" stroke="currentColor" stroke-width="4" stroke-linecap="round"/>
    <circle cx="70" cy="44" r="9" fill="none" stroke="currentColor" stroke-width="4"/>
    <path d="M22 8h8M58 8h8" stroke="currentColor" stroke-width="4" stroke-linecap="round"/>
  </svg>
  <div class="card-title">MEDICAL MALPRACTICE</div>
  <div class="card-text">For a Free Case Evaluation,<br>contact us today</div>
</div>

<div class="portrait-ring"></div>
<div class="portrait" role="img" aria-label="Portrait photo of the attorney in a dark suit and tie"></div>
<h2 class="bio-title">DANIEL R. MARLOWE, ESQUIRE</h2>
<p class="bio-sub">2006 &amp; 2007 PENNSYLVANIA RISING STAR, TOP COUNSEL</p>
<p class="bio-text" style="top:1338px">Daniel R. Marlowe has successfully handled death and serious personal injury cases involving automobiles and tractor trailers, injuries caused by toxic products, pipeline explosion cases, slip and fall cases involving commercial businesses, and cases against insurance companies.</p>
<p class="bio-text" style="top:1430px">Mr. Marlowe has been twice selected as a Pennsylvania Rising Star, Top Counsel. He serves as a Judge Pro Tem and as an arbitrator for the Court of Civil Claims, Riverton County, and is a member of the National Trial Advocates Guild and the Keystone Advocates Circle. He also serves as a Board Member for the Riverton Trial Counsel Society.</p>
<div class="btn more-btn">READ MORE INFO</div>

<section class="testimonials" role="img" aria-label="Open road through a desert toward mountains at dusk">
  <h2 class="t-title">WHAT OUR CLIENT’S SAY</h2>
  <span class="t-mark" style="left:190px;top:160px">“</span>
  <p class="t-quote">Lorem Ipsum is simply dummy text of the printing and typesetting industry. Lorem Ipsum has been the industry's standard dummy text ever since the 1500s, when an unknown printer took a galley of type and scrambled...</p>
  <span class="t-mark" style="left:706px;top:230px">”</span>
  <div class="t-name">OWEN CARTER</div>
  <div class="t-role">Business man</div>
  <div class="t-photo" role="img" aria-label="Client photo of a smiling man in glasses"></div>
  <svg class="t-arrow" style="left:108px" width="16" height="44" viewBox="0 0 16 44"><path d="M14 2 2 22l12 20" fill="none" stroke="#8a8a8a" stroke-width="2"/></svg>
  <svg class="t-arrow" style="left:1076px" width="16" height="44" viewBox="0 0 16 44"><path d="M2 2l12 20L2 42" fill="none" stroke="#8a8a8a" stroke-width="2"/></svg>
</section>

<div class="footer-col" style="left:127px">
  <div class="footer-head">WELCOME</div>
  <ul class="footer-list"><li>Home</li><li>Slip and Fall</li><li>Auto Accident</li><li>Construction Injuries</li><li>Medical Malpractice</li></ul>
</div>
<div class="footer-col" style="left:300px">
  <div class="footer-head">&nbsp;</div>
  <ul class="footer-list"><li>Results</li><li>About Us</li><li>Testimonials</li><li>Contact Us</li></ul>
</div>
<div class="footer-col" style="left:463px">
  <div class="footer-head">INFORMATION</div>
  <ul class="footer-list"><li>Terms &amp; Conditions</li><li>Privacy Policy</li><li>Disclaimer</li><li>Sitemap</li></ul>
</div>
<div class="footer-col" style="left:676px">
  <div class="footer-head">CONTACT INFO</div>
  <ul class="footer-list"><li>2200 Linden Ave #410</li><li>Riverton, PA, 19000</li>
    <li><svg width="11" height="11" viewBox="0 0 24 24" style="vertical-align:-1px;margin-right:6px"><path fill="#e8692d" d="M6.6 10.8c1.4 2.8 3.8 5.1 6.6 6.6l2.2-2.2c.3-.3.7-.4 1-.2 1.1.4 2.3.6 3.6.6.6 0 1 .4 1 1V20c0 .6-.4 1-1 1C10.6 21 3 13.4 3 4c0-.6.4-1 1-1h3.5c.6 0 1 .4 1 1 0 1.3.2 2.5.6 3.6.1.3 0 .7-.2 1z"/></svg>(555) 014-2290</li></ul>
</div>
<div class="btn email-btn">EMAIL</div>
<div class="footer-col" style="left:908px">
  <div class="footer-head">CONNECT WITH OUR<br>SOCIAL NETWORK</div>
</div>
<div class="social"><span></span><span></span><span></span><span></span><span></span></div>

<div class="footer-rule"></div>
<p class="copyright">© 2016. Harborline Injury Law Group. All rights reserved.</p>

</body>
</html>
```